Business Card Design Project

Business and Appointment Card for Medical Practice. On back of card we would like to have: blank line for patient name, Mon-Fri each with a check box next to the day, blank line for appointment date, blank line for appointment time, with option to circle am or pm.

Target Market(s)

Professional Business Associates, as well as function as patient appointment cards (on back side of card)

Industry/Entity Type

Business

Colors

Designer to choose colors to be used in the design.

```html
<!DOCTYPE html>
<html lang="en">
<head>
<meta charset="utf-8">
<title>Birch Hollow Medical Associates – Business &amp; Appointment Card</title>
<link rel="stylesheet" href="https://fonts.googleapis.com/css2?family=Marcellus+SC&display=swap">
<style>
  :root {
    --backdrop: #cfe9e1;
    --card: #ffffff;
    --green: #0f7138;
    --green-deep: #0a6431;
    --red: #b0302b;
    --rule: #4d8f62;
    --text-green: #1c6b3a;
  }
  * { margin: 0; padding: 0; box-sizing: border-box; }
  html, body {
    width: 1200px; height: 856px; overflow: hidden;
    background: var(--backdrop);
    font-family: "Marcellus SC", "Times New Roman", serif;
  }
  .card {
    position: absolute;
    width: 520px; height: 297px;
    background: var(--card);
    border-radius: 28px;
    overflow: hidden;
    box-shadow: 0 6px 18px rgba(40, 80, 70, 0.18);
  }
  .card--front { left: 50px; top: 290px; }
  .card--back  { left: 630px; top: 290px; }

  .front-art { position: absolute; inset: 0; width: 100%; height: 100%; }

  .wordmark {
    position: absolute; left: 40px; top: 92px; width: 250px;
    text-align: center; color: var(--red); line-height: 1;
  }
  .wordmark__name { display: block; font-size: 38px; letter-spacing: 0.5px; }
  .wordmark__sub { display: block; font-size: 19px; letter-spacing: 2px; margin-top: 4px; }

  .holder {
    position: absolute; left: 80px; top: 232px; color: #fff;
  }
  .holder__name { font-size: 22px; line-height: 1; }
  .holder__title { font-size: 14px; margin-top: 5px; }

  .contact {
    position: absolute; right: 34px; top: 164px; width: 200px;
    text-align: center; color: #fff; font-size: 17px; line-height: 29px;
  }

  .back-wordmark {
    position: absolute; left: 0; right: 0; top: 30px;
    text-align: center; color: var(--green); line-height: 1;
  }
  .back-wordmark__name { display: block; font-size: 17px; }
  .back-wordmark__sub { display: block; font-size: 10px; letter-spacing: 1px; margin-top: 2px; }

  .form-field {
    position: absolute; display: flex; align-items: flex-end;
    color: var(--text-green); font-size: 12px;
  }
  .form-field__line {
    display: inline-block; border-bottom: 1px solid var(--rule);
    margin-left: 10px; height: 1px; margin-bottom: 3px;
  }
  .field-patient { left: 38px; top: 108px; }
  .field-patient .form-field__line { width: 175px; }
  .field-date { left: 52px; top: 142px; }
  .field-date .form-field__line { width: 160px; }
  .field-time { left: 68px; top: 178px; }
  .field-time .form-field__line { width: 160px; }

  .meridiem {
    position: absolute; top: 199px; left: 258px;
    display: flex; gap: 48px; color: var(--text-green); font-size: 11px;
  }

  .weekdays {
    position: absolute; right: 26px; top: 88px; list-style: none;
    color: var(--text-green); font-size: 12px;
  }
  .weekdays li {
    display: flex; align-items: center; justify-content: flex-end;
    height: 22px; gap: 16px;
  }
  .weekdays li:nth-child(1) { margin-right: 0; }
  .checkbox {
    width: 17px; height: 14px; border: 1px solid var(--rule); display: inline-block;
  }
</style>
</head>
<body>

<section class="card card--front" aria-label="Business card front">
  <svg class="front-art" viewBox="0 0 520 297" aria-hidden="true">
    <path d="M0 232 C190 218 390 165 520 38 L520 297 L0 297 Z" fill="var(--green)"/>
    <path d="M20 222 C220 200 400 140 470 0 L520 0 L520 20 C400 150 200 205 40 222 Z" fill="var(--red)"/>
    <path d="M20 222 C220 200 400 140 470 0" fill="none" stroke="#fff" stroke-width="3"/>
    <path d="M0 232 C190 218 390 165 520 38" fill="none" stroke="#fff" stroke-width="3"/>
    <path d="M420 0 L456 0 C440 36 420 66 398 92 C410 60 418 30 420 0 Z" fill="var(--green-deep)"/>
  </svg>

  <div class="wordmark">
    <span class="wordmark__name">Birch Hollow</span>
    <span class="wordmark__sub">Medical Associates</span>
  </div>

  <div class="holder">
    <p class="holder__name">John Doe</p>
    <p class="holder__title">position/title</p>
  </div>

  <address class="contact" style="font-style: normal;">
    <p>123 Address Line</p>
    <p>City, State, zip</p>
    <p>555-555-5555</p>
  </address>
</section>

<section class="card card--back" aria-label="Appointment card back">
  <div class="back-wordmark">
    <span class="back-wordmark__name">Birch Hollow</span>
    <span class="back-wordmark__sub">Medical Associates</span>
  </div>

  <div class="form-field field-patient">Patient’s Name<span class="form-field__line"></span></div>
  <div class="form-field field-date">Appointment Date<span class="form-field__line"></span></div>
  <div class="form-field field-time">Appointment Time<span class="form-field__line"></span></div>
  <div class="meridiem"><span>A.M.</span><span>P.M.</span></div>

  <ul class="weekdays">
    <li>Monday <span class="checkbox"></span></li>
    <li>Tuesday <span class="checkbox"></span></li>
    <li>Wednesday <span class="checkbox"></span></li>
    <li>Thursday <span class="checkbox"></span></li>
    <li>Friday <span class="checkbox"></span></li>
  </ul>
</section>

</body>
</html>
```